R. K. Belvard & Associates, Inc

Gregor Belvard
Accountant
4219 NW 168th ST
Palmcrest, Florida 33099
(555) 555-0187
greg.belvard@quillmarsh.com
Accounting - Tax Preparation Services - Bookkeeping
Side - one business logo on the left and business information on right
On Backside: The logo in the middle and under the logo my company name.

Rounded Corner of the cards
In reference to the logo and cards I need to adjust the circle around the RK and color.

```html
<!DOCTYPE html>
<html lang="en">
<head>
<meta charset="utf-8">
<title>R. K. Belvard &amp; Associates, Inc – Business Cards</title>
<link href="https://fonts.googleapis.com/css2?family=Arimo:wght@400;700&display=swap" rel="stylesheet">
<style>
  :root {
    --brand-blue: #1172bf;
    --ink: #1f1f1f;
    --paper: #ffffff;
    --backdrop: #2a2a2c;
    --card-w: 600px;
    --card-h: 343px;
  }
  * { box-sizing: border-box; margin: 0; padding: 0; }
  html, body {
    width: 1200px; height: 900px; overflow: hidden;
    background: var(--backdrop);
    font-family: "Arimo", Arial, sans-serif;
  }
  .canvas { position: relative; width: 1200px; height: 900px; }

  .card {
    position: absolute;
    width: var(--card-w); height: var(--card-h);
    border-radius: 26px;
    overflow: hidden;
  }

  .brand-mark {
    display: flex; align-items: center; gap: 14px;
    font-weight: 700;
  }
  .brand-mark__dot {
    width: 18px; height: 18px; border-radius: 50%; flex: none;
  }

  /* Back side */
  .card--back {
    left: 470px; top: 70px;
    background: var(--brand-blue);
    display: flex; align-items: center; justify-content: center;
  }
  .card--back .brand-mark { color: var(--paper); font-size: 26px; }
  .card--back .brand-mark__dot { background: var(--paper); }

  /* Front side */
  .card--front {
    left: 150px; top: 480px;
    background: var(--paper);
  }
  .card--front .brand-mark {
    position: absolute; left: 40px; top: 0; bottom: 0;
    width: 230px;
    color: var(--ink); font-size: 22px; line-height: 1.25;
  }
  .card--front .brand-mark__dot { background: var(--brand-blue); }

  .contact {
    position: absolute; right: 48px; top: 62px;
    text-align: right; color: var(--ink);
  }
  .contact__name {
    color: var(--brand-blue); font-weight: 700;
    font-size: 27px; letter-spacing: 0.5px; text-transform: uppercase;
  }
  .contact__title { font-size: 17px; margin-top: 2px; }
  .accent-bar {
    position: absolute; right: 0; top: 84px;
    width: 16px; height: 44px; background: var(--brand-blue);
  }
  .contact__address { font-size: 16px; line-height: 1.3; margin-top: 22px; }
  .contact__line {
    font-size: 16px; line-height: 1.35;
    display: flex; justify-content: flex-end; align-items: center; gap: 8px;
  }
  .contact__line--first { margin-top: 6px; }
  .icon { width: 14px; height: 14px; fill: var(--brand-blue); flex: none; }
  .services { list-style: none; margin-top: 22px; font-size: 16px; line-height: 1.4; }
  .services li { display: flex; justify-content: flex-end; align-items: center; gap: 9px; }
  .services li::after {
    content: ""; width: 6px; height: 6px; border-radius: 50%;
    background: var(--brand-blue);
  }
</style>
</head>
<body>
<main class="canvas">

  <section class="card card--back" aria-label="Card back">
    <div class="brand-mark">
      <span class="brand-mark__dot"></span>
      <span>R. K. Belvard &amp; Associates, Inc</span>
    </div>
  </section>

  <section class="card card--front" aria-label="Card front">
    <div class="brand-mark">
      <span class="brand-mark__dot"></span>
      <span>R. K. Belvard &amp; Associates, Inc</span>
    </div>

    <span class="accent-bar"></span>

    <div class="contact">
      <h1 class="contact__name">Gregor Belvard</h1>
      <p class="contact__title">Accountant</p>
      <p class="contact__address">4219 NW 168th ST<br>Palmcrest, Florida 33099</p>
      <p class="contact__line contact__line--first">(555) 555-0187
        <svg class="icon" viewBox="0 0 24 24" aria-hidden="true"><path d="M6.6 10.8a15.1 15.1 0 0 0 6.6 6.6l2.2-2.2a1 1 0 0 1 1-.25 11.4 11.4 0 0 0 3.6.57 1 1 0 0 1 1 1V20a1 1 0 0 1-1 1A17 17 0 0 1 3 4a1 1 0 0 1 1-1h3.5a1 1 0 0 1 1 1c0 1.25.2 2.45.57 3.57a1 1 0 0 1-.25 1z"/></svg>
      </p>
      <p class="contact__line">greg.belvard@quillmarsh.com
        <svg class="icon" viewBox="0 0 24 24" aria-hidden="true"><path d="M2 5h20v14H2z M2 5l10 8 10-8" fill="var(--brand-blue)" stroke="#fff" stroke-width="1.5"/></svg>
      </p>
      <ul class="services">
        <li>Accounting</li>
        <li>Tax Preparation Services</li>
        <li>Bookkeeping</li>
      </ul>
    </div>
  </section>

</main>
</body>
</html>
```